The Marrow Lanterns Podcast

A logo that defines defiance. The "Marrow Lanterns" Podcast with Brent & Quill will revolve around people who have accomplished remarkable things in spite of odds being stacked against them. I want the logo to be simple, marketable, strong and bold, attractive to the eye on a mobile device. The hosts name will be part of the logo. I will give you full creative freedom to the artists to try to create something that is truly legendary and amazing. Please feel free to reach out if you have any questions.Podcast name: The Defying OnesHosts: Brent & Quill
Target Market(s)
Listeners interested in self growth, excitement, inspiration, fun.
Colors
Designer to choose colors to be used in the design.
Look and feel

```html
<!DOCTYPE html>
<html lang="en">
<head>
<meta charset="utf-8">
<title>The Marrow Lanterns Podcast</title>
<link rel="stylesheet" href="https://fonts.googleapis.com/css2?family=Cabin:wght@400;500&display=swap">
<style>
  :root {
    --page: #ffffff;
    --band: rgba(12, 10, 12, 0.88);
    --ink-light: #ffffff;
    --ink-gold: #f6e21a;
    --ink-pale-gold: #fbf3a0;
    --sky-glow: #fff3c4;
    --amber: #e8a23a;
    --rust: #8a4a18;
    --moss: #3b3f18;
    --shade: #0d0b08;
  }
  * { margin: 0; padding: 0; box-sizing: border-box; }
  html, body { width: 1200px; height: 1179px; overflow: hidden; background: var(--page); }
  .canvas { position: relative; width: 1200px; height: 1179px; }
  .cover {
    position: absolute; left: 30px; top: 19px; width: 1137px; height: 1135px;
    overflow: hidden; border-radius: 3px;
    box-shadow: 0 4px 14px rgba(0,0,0,0.45);
    font-family: "Cabin", "Gill Sans", sans-serif;
  }
  .forest-scene {
    position: absolute; inset: 0;
    background:
      radial-gradient(ellipse 45% 40% at 50% 12%, var(--sky-glow) 0%, rgba(255,220,140,0.6) 40%, transparent 75%),
      linear-gradient(180deg, #c98a3c 0%, var(--amber) 30%, var(--rust) 55%, var(--moss) 72%, var(--shade) 100%);
  }
  .lower-shade {
    position: absolute; left: 0; right: 0; bottom: 0; height: 420px;
    background: linear-gradient(180deg, transparent 0%, rgba(10,9,6,0.55) 45%, rgba(10,9,6,0.85) 100%);
  }
  .hosts-band {
    position: absolute; left: 0; right: 0; top: 37px; height: 72px;
    background: var(--band);
    display: flex; align-items: center; justify-content: center;
  }
  .hosts {
    color: var(--ink-light); font-weight: 400; font-size: 62px; letter-spacing: 1px; line-height: 1;
  }
  .hosts .amp { font-size: 42px; margin: 0 10px; }
  .title-block { position: absolute; left: 50px; top: 752px; width: 1060px; }
  .title-the {
    display: block; font-size: 90px; font-weight: 400; line-height: 1;
    color: var(--ink-pale-gold);
  }
  .title-name {
    display: block; font-size: 102px; font-weight: 400; line-height: 1; margin-top: 8px;
    letter-spacing: -1px; white-space: nowrap; color: var(--ink-light);
  }
  .title-name .accent { color: var(--ink-gold); }
  .title-podcast {
    display: block; font-size: 96px; font-weight: 400; line-height: 1; margin-top: 2px;
    color: var(--ink-light);
  }
</style>
</head>
<body>
  <main class="canvas">
    <section class="cover">
      <div class="forest-scene" role="img" aria-label="Sunlit misty pine forest with a lone figure silhouetted among tall trunks"></div>
      <div class="lower-shade"></div>
      <header class="hosts-band">
        <p class="hosts">BRENT<span class="amp">&amp;</span>QUILL</p>
      </header>
      <h1 class="title-block">
        <span class="title-the">The</span>
        <span class="title-name">MARROW <span class="accent">LANTERNS</span></span>
        <span class="title-podcast">PODCAST</span>
      </h1>
    </section>
  </main>
</body>
</html>
```